Healthcare Review Meeting

We are a manufacturing company that provides health insurance to our 230+ employees. We have been trying to educate them on understanding and utilizing their healthcare benefits. We would like to reach out to the spouses to provide them with the same information. We are a predominately male company and we want to reach the spouses, who likely make all the healthcare decisions. I attached a sample of what we are looking for, but it needs some sprucing up.

```html
<!DOCTYPE html>
<html lang="en">
<head>
<meta charset="utf-8">
<title>Understanding Your Health Insurance – Event Postcard</title>
<link rel="stylesheet" href="https://fonts.googleapis.com/css2?family=Questrial&family=Oswald:wght@400&display=swap">
<style>
  :root {
    --page-bg: #2a2a2a;
    --card-white: #ffffff;
    --green: #5cb94e;
    --green-light: #a6d874;
    --green-pale: #d6edbd;
    --navy: #24338a;
    --logo-navy: #1f2e5c;
    --ink: #222222;
    --panel-top: #eaf4fa;
    --panel-bottom: #c9e6ee;
    --rule: #555555;
  }
  * { margin: 0; padding: 0; box-sizing: border-box; }
  html, body { width: 900px; height: 1200px; overflow: hidden; }
  body {
    background: var(--page-bg);
    font-family: "Questrial", "Century Gothic", sans-serif;
    position: relative;
  }
  .card {
    position: absolute;
    background: var(--card-white);
  }
  .card--front { left: 98px; top: 37px; width: 705px; height: 545px; }
  .card--back  { left: 97px; top: 617px; width: 706px; height: 546px; }

  /* Front */
  .hero {
    position: absolute; left: 23px; top: 23px; width: 659px; height: 499px;
    background: radial-gradient(circle at 35% 60%, #eef7e2 0%, var(--green-pale) 35%, var(--green-light) 80%, #8cc850 100%);
  }
  .hero__visual {
    position: absolute; left: 80px; top: 70px; width: 300px; height: 360px;
    border-radius: 48% 48% 46% 46%;
    background: radial-gradient(circle at 45% 40%, #a4dc6a 0%, #6fbf3c 55%, #4f9e2a 100%);
  }
  .tag {
    position: absolute;
    background: var(--green);
    color: #fff;
    font-family: "Oswald", "Arial Narrow", sans-serif;
    font-size: 36px;
    line-height: 1;
    letter-spacing: 0.5px;
    white-space: nowrap;
  }
  .tag--health { left: 0; top: 271px; width: 165px; height: 48px; padding: 6px 0 0 17px; }
  .tag--insurance { left: 180px; top: 324px; width: 196px; height: 44px; padding: 4px 0 0 12px; font-size: 34px; }
  .headline-box {
    position: absolute; left: 399px; top: 118px; width: 306px; height: 310px;
    background: var(--green);
  }
  .headline-box__frame {
    position: absolute; left: 11px; top: 12px; width: 284px; height: 285px;
    border: 3px solid #fff;
    color: #fff;
    text-align: center;
  }
  .headline { font-weight: 400; margin-top: 28px; line-height: 1; }
  .headline__line1 { display: block; font-size: 27px; letter-spacing: 0.5px; }
  .headline__line2 { display: block; font-size: 38px; margin-top: 8px; }
  .headline__your { font-size: 27px; border-bottom: 2px solid #fff; }
  .headline__line3 { display: block; font-size: 40px; margin-top: 6px; }
  .headline-box__rule {
    width: 220px; height: 1px; margin: 32px auto 0;
    background: linear-gradient(90deg, transparent, #fff, transparent);
  }
  .headline-box__sub { font-size: 21px; line-height: 1.4; margin-top: 20px; }

  /* Back */
  .info-panel {
    position: absolute; left: 24px; top: 25px; width: 361px; height: 496px;
    background: linear-gradient(135deg, var(--panel-top) 0%, var(--panel-bottom) 100%);
  }
  .company-name { position: absolute; left: 20px; top: 16px; color: var(--navy); font-size: 24px; white-space: nowrap; }
  .company-address { position: absolute; left: 20px; top: 52px; color: var(--ink); font-size: 23px; line-height: 1.35; white-space: nowrap; }
  .event-band {
    position: absolute; left: 0; top: 151px; width: 347px; height: 214px;
    background: var(--green);
  }
  .event-band__frame {
    position: absolute; left: 20px; top: 15px; width: 313px; height: 185px;
    border: 3px solid #fff; color: #fff;
    padding: 12px 0 0 24px;
  }
  .event-band__invite { font-size: 23px; line-height: 1.3; }
  .event-band__when { font-size: 22px; line-height: 1.36; margin-top: 8px; }
  .rsvp { position: absolute; left: 20px; top: 352px; font-size: 22px; line-height: 1.42; white-space: nowrap; }
  .rsvp__name { color: var(--navy); }
  .rsvp__phone { color: var(--ink); }
  .brand-mark {
    position: absolute; left: 22px; top: 430px;
    display: flex; align-items: center; gap: 10px;
    color: var(--logo-navy); font-size: 24px; line-height: 1.05;
    white-space: nowrap;
  }
  .brand-mark__square { width: 46px; height: 46px; background: var(--logo-navy); flex: none; }
  .stamp-box {
    position: absolute; left: 587px; top: 38px; width: 82px; height: 91px;
    border: 1px solid var(--rule);
  }
  .address-lines { position: absolute; left: 428px; top: 310px; width: 241px; }
  .address-lines span { display: block; height: 1px; background: var(--rule); margin-bottom: 37px; }
</style>
</head>
<body>
  <section class="card card--front">
    <div class="hero">
      <div class="hero__visual" role="img" aria-label="Green apple with a red question mark in front of a faint stethoscope"></div>
      <div class="tag tag--health">HEALTH</div>
      <div class="tag tag--insurance">INSURANCE</div>
    </div>
    <div class="headline-box">
      <div class="headline-box__frame">
        <h1 class="headline">
          <span class="headline__line1">UNDERSTANDING</span>
          <span class="headline__line2"><span class="headline__your">YOUR</span> HEALTH</span>
          <span class="headline__line3">INSURANCE</span>
        </h1>
        <div class="headline-box__rule"></div>
        <p class="headline-box__sub">Come Join Us And<br>We Will Explain It!</p>
      </div>
    </div>
  </section>

  <section class="card card--back">
    <div class="info-panel">
      <p class="company-name">Keystone Metalworks Inc.</p>
      <p class="company-address">48 Foundry Lane Millbrook,<br>NJ 08000</p>
      <p class="rsvp"><span class="rsvp__name">RSVP: Dana Whitfield</span><br><span class="rsvp__phone">(555) 014-2200 Ext 1042</span></p>
      <div class="brand-mark"><span class="brand-mark__square"></span><span>KEYSTONE<br>METALWORKS</span></div>
    </div>
    <div class="event-band">
      <div class="event-band__frame">
        <p class="event-band__invite">PLEASE JOIN US<br>FOR THIS EVENT</p>
        <p class="event-band__when">APRIL 2, 2016<br>10:00am to 12:00pm<br>or 2:00pm to 4:00pm</p>
      </div>
    </div>
    <div class="stamp-box"></div>
    <div class="address-lines"><span></span><span></span><span></span></div>
  </section>
</body>
</html>
```